Postcard Design

Company Name--motion harbor
482 Garnet Avenue
Brooklyn New York11231
347-555-0182
www.motionharbors. example
We are a boutique personal fitness company in a exclusive neighnorhood in Brooklyn New York. We specialize in personal training and innovate new fitness classes such as Pulse-Circuit QVR and Tabata.

We want our brand to be high-end but open to all. Laid-back but experts in the field of fitness. Innovative and flexible. Proffessional, friendly and inspiring.

Personal attention for our clients is a must as well as making sure they succeed. 87% of our clients reach their goals.

Colors should be bright but sophisticated with a little aggression but not intimidation.
Updates

Company Name-And contact info has been updated on the brief

I posted a logo. And the colors on the website have changed. If you could incorporate the website color scheme that would be helpful. If for whatever reason the logo is not here I will try to upload again.

Change the contact info: www.motionharbors.example You tube: Brisco and the Motion Harbor Email: Motionharbors@mailbox.example Verbiage changes: 'The only boutique personal fitness studio in Brooklyn. Featuring uniquely proprietary classes QVR, Cross Training and now Tabata." Verbiage Additions Safe for moms, dads and we offer enhanced childcare with certified child care development teachers with our partner studios. Classes start at $15

Please Add : Use this postcard to receive 10% any service

Hi, I could not upload the logo. However they said that our Logo should be uploaded now as I sent it to them manually.

Target Market(s)

30-40 year old women and new moms looking to do cross fit and personal training. Income 80-85K.

Industry/Entity Type

Boutique

Requirements
Must have
• Highlight Tabata and the excellence of the classes.Tag lines- Increase calorie burn by 20%. Increase muscle tone by 25%.Increase metabolism by 25%. Classes only available by appointment. 30mins or 1 hour.
Nice to have
• Attractive and fit young people having fun. Personal training.
Should not have
• Overly sexual fitness models.

```html
<!DOCTYPE html>
<html lang="en">
<head>
<meta charset="utf-8">
<title>Motion Harbor Postcard</title>
<link href="https://fonts.googleapis.com/css2?family=Oswald:wght@500;600&family=Roboto+Condensed:ital,wght@0,400;0,700;1,700&display=swap" rel="stylesheet">
<style>
  :root {
    --backdrop: #5c5d5f;
    --card: #ffffff;
    --sun: #fdd20a;
    --plum: #a3125f;
    --hot-pink: #e6168a;
    --ink: #1d1d1b;
    --alert-red: #d7262e;
    --photo-light: #d9c2b4;
    --photo-dark: #3a2a24;
    --iron: #2b2b2b;
  }
  * { margin: 0; padding: 0; box-sizing: border-box; }
  html, body { width: 1200px; height: 962px; overflow: hidden; background: var(--backdrop); }
  .stage { position: relative; width: 1200px; height: 962px; }
  .postcard {
    position: absolute; left: 66px; top: 74px; width: 1068px; height: 814px;
    background: var(--card);
    box-shadow: 0 14px 30px rgba(0,0,0,.45);
  }
  .brand {
    position: absolute; left: 110px; top: 140px;
    font-family: "Oswald", sans-serif; font-weight: 600; color: var(--ink);
    line-height: 1; letter-spacing: 4px;
  }
  .brand-main { display: block; font-size: 76px; }
  .brand-sub { display: block; font-size: 30px; letter-spacing: 12px; margin-top: 8px; }
  .benefits {
    position: absolute; left: 462px; top: 138px; width: 250px;
    font-family: "Roboto Condensed", sans-serif; font-size: 17px; line-height: 22px; color: var(--plum);
    list-style: none;
  }
  .benefits li { font-weight: 700; }
  .benefits .booking { font-weight: 400; color: var(--ink); margin-top: 4px; }
  .offer-panel {
    position: absolute; left: 98px; top: 288px; width: 992px; height: 380px;
    background: var(--sun); border-top-right-radius: 18px;
  }
  .register-band {
    position: absolute; left: 115px; top: 662px; width: 990px; height: 134px;
    background: var(--plum);
  }
  .model-photo {
    position: absolute; left: 720px; top: 112px; width: 405px; height: 660px;
    background: linear-gradient(160deg, var(--photo-dark) 0%, var(--photo-light) 35%, #f2f2f2 70%, var(--photo-light) 100%);
    border-radius: 180px 120px 0 0;
  }
  .dumbbell-photo {
    position: absolute; left: 640px; top: 368px; width: 190px; height: 195px;
    background: radial-gradient(circle at 45% 45%, #555 0%, var(--iron) 55%, #111 100%);
    border-radius: 50%;
  }
  .intro {
    position: absolute; left: 130px; top: 312px;
    font-family: "Roboto Condensed", sans-serif; font-weight: 700;
    font-size: 25px; line-height: 34px; color: var(--plum);
  }
  .headline {
    position: absolute; left: 133px; top: 402px;
    font-family: "Oswald", sans-serif; font-weight: 600; color: var(--plum);
    text-transform: uppercase; line-height: 1;
  }
  .headline-line { display: block; font-size: 48px; }
  .headline-now { font-size: 44px; vertical-align: top; position: relative; top: 14px; }
  .headline-feature { font-size: 100px; margin-left: 10px; letter-spacing: 2px; }
  .headline-row { display: block; margin-top: -4px; }
  .childcare {
    position: absolute; left: 135px; top: 582px; width: 500px;
    font-family: "Roboto Condensed", sans-serif; font-size: 20px; line-height: 24px; color: var(--ink);
  }
  .register-title {
    position: absolute; left: 142px; top: 694px;
    font-family: "Roboto Condensed", sans-serif; font-weight: 700; font-style: italic;
    font-size: 40px; color: #fff; letter-spacing: .5px;
  }
  .contact {
    position: absolute; left: 140px; top: 742px;
    font-family: "Roboto Condensed", sans-serif; font-weight: 700; font-style: italic;
    font-size: 24px; color: var(--sun); word-spacing: 2px;
  }
  .contact span + span { margin-left: 22px; }
  .price-badge {
    position: absolute; left: 886px; top: 642px; width: 196px; height: 196px;
    border-radius: 50%; background: var(--hot-pink); border: 5px solid #fff;
    text-align: center; font-family: "Oswald", sans-serif; font-weight: 600;
  }
  .price-label { display: block; color: #fff; font-size: 28px; line-height: 28px; margin-top: 24px; }
  .price-value { display: block; color: var(--sun); font-size: 74px; line-height: 80px; }
  .price-currency { font-size: 44px; vertical-align: top; position: relative; top: 6px; }
  .postcard-discount {
    position: absolute; left: 127px; top: 810px;
    font-family: "Roboto Condensed", sans-serif; font-size: 25px; color: var(--ink);
  }
  .postcard-discount strong { color: var(--alert-red); font-weight: 700; }
  .address {
    position: absolute; left: 127px; top: 848px;
    font-family: "Roboto Condensed", sans-serif; font-size: 17px; color: var(--ink);
  }
</style>
</head>
<body>
<div class="stage">
  <div class="postcard"></div>

  <div class="brand">
    <span class="brand-main">MOTION</span>
    <span class="brand-sub">HARBOR</span>
  </div>

  <ul class="benefits">
    <li>Increase calorie burn by 20%</li>
    <li>Increase muscle tone by 25%</li>
    <li>Increase metabolism by 25%</li>
    <li class="booking">Classes by appointment only<br>30 mins or 1 hour</li>
  </ul>

  <div class="offer-panel"></div>
  <div class="register-band"></div>

  <div class="model-photo" role="img" aria-label="Photo of a smiling woman in a white tank top lifting a dumbbell"></div>
  <div class="dumbbell-photo" role="img" aria-label="Photo of a black weight plate dumbbell"></div>

  <p class="intro">The only boutique personal fitness studio in Brooklyn.<br>Featuring uniquely proprietary classes</p>

  <h1 class="headline">
    <span class="headline-line">QVR, Cross Training</span>
    <span class="headline-row"><span class="headline-now">&amp; Now</span><span class="headline-feature">Tabata</span></span>
  </h1>

  <p class="childcare">Safe for moms, dads and we offer enhanced childcare with certified child care development teachers with our partner studios.</p>

  <p class="register-title">REGISTER TODAY!!</p>
  <p class="contact"><span>347-555-0182</span><span>WWW.MOTIONHARBORS.EXAMPLE</span></p>

  <div class="price-badge">
    <span class="price-label">CLASSES<br>START AT</span>
    <span class="price-value"><span class="price-currency">$</span>15</span>
  </div>

  <p class="postcard-discount">USE THIS POSTCARD TO RECEIVE <strong>10% OFF</strong> ON ANY SERVICE</p>
  <p class="address">482 Garnet Avenue, Brooklyn, New York 11231</p>
</div>
</body>
</html>
```